Internet of Things integrator needs logo and website design

We need a logo and website design for our company ("Brightwave Link"). We integrate IoT(Internet of Things) projects including: devices, network and sw solutions for all type of vertical markets. The image should be professional like the following site: quorvel.io clear and easy surfing, and should include about the same sections shown in that website (Why Us?, Products, Resources, Company, etc). Website colors should follow logo colors (logo has to be designed and aproved first). The logo should be something like the one used at tandemvexa.com (image attached), where we could use the logo to susbtitute the letter "o" in "IoT". The final design should communicate professionalism and experience.

Coding

Coded - Design and coding required

Number of Pages Required

5+ page

Font styles to use
Other font styles liked:
• see quorvel.io wensite

Requirements
Must have
• Serious and professional look and feel as in: quorvel.io website.
The following pages should be included:
- home page
- Why Us?
- Products
- Resources
- Company
- Newsroom
- Contact
Nice to have
• High tech look and feel
Should not have
• Fun or not serious images (cartoons, etc.)

```html
<!DOCTYPE html>
<html lang="en">
<head>
<meta charset="utf-8">
<title>Brightwave Link – Industrial Edge Computing Platform</title>
<link href="https://fonts.googleapis.com/css2?family=Ubuntu:wght@400;500;700&display=swap" rel="stylesheet">
<style>
:root{
  --navy:#13207e;
  --navy-dark:#0d1766;
  --accent:#fc2a57;
  --ink:#151515;
  --muted:#777;
  --card:#f4f4f4;
  --tint:#eaf1fd;
  --dot:#4a7cf0;
  --white:#fff;
  --star:#f5a623;
}
*{margin:0;padding:0;box-sizing:border-box}
html,body{width:1200px;height:4448px;overflow:hidden}
body{position:relative;background:var(--white);font-family:"Ubuntu",sans-serif;color:var(--ink)}
.abs{position:absolute}
.btn{position:absolute;background:var(--accent);color:var(--white);font-size:15px;display:flex;align-items:center;justify-content:center}
.brand{display:flex;align-items:center;gap:10px;font-weight:700;letter-spacing:.5px}
.brand .mark{width:22px;height:22px;border-radius:50%;border:3px solid var(--accent)}
.nav{position:absolute;display:flex;font-size:11.5px;color:#555}
.nav span{position:absolute;white-space:nowrap}
.dots{position:absolute;background-image:radial-gradient(circle,var(--dot) 2px,transparent 2.5px);background-size:14px 13px}
.h2{position:absolute;font-size:35px;font-weight:500}
.copy{position:absolute;font-size:11.5px;line-height:22.5px;color:#666}
.photo{position:absolute}
/* header */
.header-logo{left:164px;top:28px;font-size:26px;color:var(--navy)}
.phone-btn{left:1002px;top:26px;width:36px;height:36px;background:var(--accent);display:flex;align-items:center;justify-content:center}
/* hero */
.hero{left:0;top:98px;width:788px;height:712px;background:var(--navy)}
.hero-title{left:162px;top:312px;font-size:44px;line-height:50px;font-weight:500;color:var(--white)}
.hero-text{left:162px;top:421px;font-size:12px;line-height:22px;color:var(--white)}
.hero-photo{left:713px;top:195px;width:430px;height:523px;border-radius:40px 40px 0 40px;background:linear-gradient(160deg,#0f2d57,#1f5ea0 45%,#6cb5c7)}
/* why */
.why-photo{left:162px;top:900px;width:337px;height:411px;border-radius:40px 40px 40px 0;background:linear-gradient(170deg,#4f86d0,#9dbbe0 50%,#7d6f9a)}
/* products */
.product{position:absolute;top:1466px;width:323px;height:435px;background:var(--card)}
.product .icon{position:absolute;left:14px;top:42px}
.product h3{position:absolute;left:14px;top:146px;font-size:19px;font-weight:500}
.product .sub{position:absolute;left:14px;top:180px;font-size:12px;color:var(--accent)}
.product p{position:absolute;left:14px;top:222px;width:300px;font-size:11px;line-height:23px;color:#666}
.product .btn{left:12px;top:361px;width:119px;height:40px;font-size:13.5px}
/* resources */
.res-card{left:409px;top:2122px;width:501px;height:239px;background:var(--white);box-shadow:0 0 12px rgba(0,0,0,.08)}
.res-book{left:43px;top:31px;width:118px;height:182px;background:linear-gradient(90deg,#e4e4e4,#fafafa 30%,#dcdcdc)}
.res-photo{left:0;top:2228px;width:349px;height:487px;border-radius:0 40px 40px 0;background:linear-gradient(150deg,#123a4e,#2b8a9c 45%,#c9b25a)}
.tint{left:249px;top:2490px;width:951px;height:757px;background:var(--tint);border-radius:0 0 0 40px}
.clients{left:302px;top:2425px;width:674px;height:148px;background:var(--navy);border-radius:6px;display:flex;align-items:center;justify-content:space-around;color:var(--white);font-size:16px;font-weight:500;letter-spacing:1px}
.arrow{position:absolute;width:36px;height:36px;border:2px solid var(--accent);border-radius:3px;display:flex;align-items:center;justify-content:center}
/* testimonials */
.quote{position:absolute;top:2917px;width:278px;height:195px;background:var(--white);box-shadow:0 0 10px rgba(0,0,0,.08)}
.quote .avatar{position:absolute;left:20px;top:22px;width:50px;height:50px;border-radius:50%;background:linear-gradient(160deg,#c8ccd3,#3d4a5e)}
.quote .name{position:absolute;left:90px;top:32px;font-size:15px;font-weight:500}
.quote .role{position:absolute;left:90px;top:54px;font-size:10.5px;color:var(--accent)}
.quote .mark{position:absolute;right:18px;top:26px;font-size:34px;color:#ccc;line-height:1;font-weight:700}
.quote p{position:absolute;left:17px;top:89px;width:255px;font-size:10.5px;line-height:19px;color:#666}
.quote .stars{position:absolute;left:17px;top:148px;font-size:14px;color:var(--star);letter-spacing:1px}
/* news */
.news-photo{left:782px;top:3178px;width:418px;height:777px;border-radius:40px 0 0 40px;background:linear-gradient(150deg,#1c2226,#3d4a4f 50%,#c9cfd3)}
.news{position:absolute;width:278px;height:242px;background:var(--white);box-shadow:0 0 10px rgba(0,0,0,.07)}
.news h4{position:absolute;left:16px;top:28px;font-size:14px;font-weight:500}
.news p{position:absolute;left:16px;top:56px;width:235px;font-size:11px;line-height:22.5px;color:#666}
.news .btn{left:15px;top:170px;width:119px;height:38px;font-size:13.5px}
/* footer */
.footer{left:0;top:4086px;width:1200px;height:311px;background:var(--navy)}
.footer-logo{left:0;width:1200px;top:4154px;justify-content:center;font-size:30px;color:var(--white)}
.footer-logo .mark{border-color:var(--white)}
.footer-rule{left:161px;top:4266px;width:878px;height:1px;background:rgba(255,255,255,.3)}
.follow{left:0;width:1200px;top:4289px;text-align:center;font-size:14px;font-weight:500;color:var(--white)}
.social{position:absolute;top:4323px;width:37px;height:37px;border:1.5px solid var(--white);display:flex;align-items:center;justify-content:center}
.social i{width:8px;height:8px;background:var(--white);border-radius:50%}
.social.active{background:var(--accent);border-color:var(--accent)}
.legal{left:0;top:4397px;width:1200px;height:51px;background:var(--navy-dark);color:var(--white);font-size:10.5px;display:flex;align-items:center;justify-content:center}
</style>
</head>
<body>

<!-- header -->
<div class="abs brand header-logo">BRIGHTWAVE LINK <span class="mark"></span></div>
<nav class="nav" style="left:0;top:37px">
  <span style="left:597px">Home</span><span style="left:653px">Why Us?</span><span style="left:722px">Products</span><span style="left:793px">Resources</span><span style="left:872px">News</span><span style="left:929px">Contact Us</span>
</nav>
<div class="abs phone-btn"><svg width="18" height="18" viewBox="0 0 24 24"><path d="M6.6 10.8a15 15 0 0 0 6.6 6.6l2.2-2.2c.3-.3.7-.4 1-.2 1.1.4 2.3.6 3.6.6.6 0 1 .4 1 1V20c0 .6-.4 1-1 1A17 17 0 0 1 3 4c0-.6.4-1 1-1h3.5c.6 0 1 .4 1 1 0 1.3.2 2.5.6 3.6.1.3 0 .7-.2 1z" fill="#fff"/></svg></div>

<!-- hero -->
<section class="abs hero"></section>
<h1 class="abs hero-title">INDUSTRIAL EDGE<br>COMPUTING PLATFORM</h1>
<p class="abs hero-text">Lorem Ipsum is simply dummy text of the printing and typesetting industry.<br>Lorem Ipsum has been the industry's standard dummy text ever since the 1500s,</p>
<div class="btn" style="left:161px;top:525px;width:195px;height:52px;font-size:18px;font-weight:500">Free Consulting</div>
<div class="photo hero-photo" role="img" aria-label="Smiling engineer holding a tablet in a server room"></div>
<div class="dots" style="left:1100px;top:677px;width:88px;height:84px"></div>

<!-- why us -->
<div class="photo why-photo" role="img" aria-label="Businesswoman with hard hat and tablet overlooking a city with connected-device icons"></div>
<div class="dots" style="left:117px;top:1275px;width:88px;height:78px"></div>
<h2 class="h2" style="left:613px;top:924px">Why Us?</h2>
<p class="copy" style="left:613px;top:985px;width:380px">Lorem Ipsum is simply dummy text of the printing and typesetting industry. Lorem Ipsum has been the industry's standard dummy text ever since the 1500s, when an unknown printer took a galley of type and scrambled it to make a type specimen book. It has survived not only five centuries, but also the leap into electronic typesetting, remaining essentially unchanged. It was popularised in the 1960s with the release of Letraset sheets containing Lorem Ipsum passages, and more recently with desktop publishing software like Aldus PageMaker including versions of Lorem Ipsum.</p>
<div class="btn" style="left:611px;top:1235px;width:120px;height:40px">Read More</div>

<!-- products -->
<h2 class="h2" style="left:0;width:1200px;text-align:center;top:1382px">Our Products</h2>
<article class="product" style="left:266px">
  <svg class="icon" width="76" height="62" viewBox="0 0 76 62" fill="none" stroke="#fc2a57" stroke-width="2.5"><path d="M18 40a12 12 0 0 1 2-24 17 17 0 0 1 32-3 13 13 0 0 1 6 27z"/><rect x="24" y="32" width="26" height="16" rx="2"/><path d="M37 48v7M28 57h18"/></svg>
  <h3>Brightwave Edge</h3>
  <div class="sub">Industrial Edge Computing Platform</div>
  <p>Lorem Ipsum is simply dummy text of the printing and typesetting industry. Lorem Ipsum has been the industry's standard dummy text ever since the 1500s, when an unknown printer took a galley of type and scrambled it to make a type specimen book.</p>
  <div class="btn">Read More</div>
</article>
<article class="product" style="left:611px">
  <svg class="icon" width="76" height="62" viewBox="0 0 76 62" fill="none" stroke="#fc2a57" stroke-width="2.5"><rect x="10" y="22" width="40" height="26" rx="3"/><path d="M3 52h54l-4 5H7z"/><path d="M54 12a10 10 0 0 1 8 8M54 4a18 18 0 0 1 16 16"/></svg>
  <h3>Brightwave Edge Manager</h3>
  <div class="sub">Edge Device Lifecycle Management</div>
  <p>Lorem Ipsum is simply dummy text of the printing and typesetting industry. Lorem Ipsum has been the industry's standard dummy text ever since the 1500s, when an unknown printer took a galley of type and scrambled it to make a type specimen book.</p>
  <div class="btn">Read More</div>
</article>

<!-- resources -->
<h2 class="h2" style="left:418px;top:1974px">Resorces</h2>
<p class="copy" style="left:418px;top:2022px;width:515px;font-size:11px;line-height:19.5px">Lorem Ipsum is simply dummy text of the printing and typesetting industry. Lorem Ipsum has been the industry's standard dummy text ever since the 1500s, when an unknown printer took a galley of type and scrambled it to make a type specimen book.</p>
<div class="tint abs"></div>
<article class="abs res-card">
  <div class="abs res-book" role="img" aria-label="Whitepaper book cover"></div>
  <div class="abs" style="left:207px;top:24px;font-size:15px;font-weight:500">Resource Name 1</div>
  <div class="abs" style="left:207px;top:46px;font-size:11px;color:var(--accent)">Internet of Things</div>
  <p class="copy" style="left:207px;top:73px;width:255px;font-size:11px;line-height:22.5px">Lorem Ipsum is simply dummy text of the printing and typesetting industry. Lorem Ipsum has been the industry's standard dummy text ever since the 1500s, when an unknown printer took a galley of type and scrambled it to make a type specimen book.</p>
</article>
<div class="photo res-photo" role="img" aria-label="Smart city skyline with network connection overlay"></div>
<div class="abs clients">
  <span>NORTHGATE</span><span style="font-weight:400;font-size:13px">HALVERN &amp; STROUD</span><span style="font-size:14px">Kasumi Works</span><span style="font-size:14px">Ferrovia Legal</span>
</div>
<div class="arrow" style="left:387px;top:2618px"><svg width="12" height="20" viewBox="0 0 12 20" fill="none" stroke="#fc2a57" stroke-width="2"><path d="M10 2 2 10l8 8"/></svg></div>
<div class="arrow" style="left:447px;top:2618px"><svg width="12" height="20" viewBox="0 0 12 20" fill="none" stroke="#fc2a57" stroke-width="2"><path d="m2 2 8 8-8 8"/></svg></div>
<div class="dots" style="left:43px;top:2725px;width:88px;height:31px"></div>

<!-- testimonials -->
<h2 class="h2" style="left:342px;top:2750px">Testimonials</h2>
<p class="copy" style="left:342px;top:2808px;width:510px;font-size:11px;line-height:19.5px">Lorem Ipsum is simply dummy text of the printing and typesetting industry. Lorem Ipsum has been the industry's standard dummy text ever since the 1500s, when an unknown printer took a galley of type and scrambled it to make a type specimen book.</p>
<div class="arrow" style="left:941px;top:2820px"><svg width="12" height="20" viewBox="0 0 12 20" fill="none" stroke="#fc2a57" stroke-width="2"><path d="M10 2 2 10l8 8"/></svg></div>
<div class="arrow" style="left:1002px;top:2820px"><svg width="12" height="20" viewBox="0 0 12 20" fill="none" stroke="#fc2a57" stroke-width="2"><path d="m2 2 8 8-8 8"/></svg></div>

<article class="quote" style="left:161px"><div class="avatar" role="img" aria-label="Client portrait"></div><div class="name">Client Name</div><div class="role">Client Designation</div><div class="mark">”</div><p>Lorem Ipsum is simply dummy text of the printing and typesetting industry. Lorem Ipsum has been the industry's standard dummy text.</p><div class="stars">★★★★☆</div></article>
<article class="quote" style="left:461px"><div class="avatar" role="img" aria-label="Client portrait"></div><div class="name">Client Name</div><div class="role">Client Designation</div><div class="mark">”</div><p>Lorem Ipsum is simply dummy text of the printing and typesetting industry. Lorem Ipsum has been the industry's standard dummy text.</p><div class="stars">★★★★☆</div></article>
<article class="quote" style="left:761px"><div class="avatar" role="img" aria-label="Client portrait"></div><div class="name">Client Name</div><div class="role">Client Designation</div><div class="mark">”</div><p>Lorem Ipsum is simply dummy text of the printing and typesetting industry. Lorem Ipsum has been the industry's standard dummy text.</p><div class="stars">★★★★☆</div></article>

<!-- news -->
<div class="photo news-photo" role="img" aria-label="Developer working on laptop and monitors showing code"></div>
<div class="dots" style="left:1038px;top:3965px;width:88px;height:36px"></div>
<h2 class="h2" style="left:0;width:1200px;text-align:center;top:3306px">Latest News</h2>

<article class="news" style="left:161px;top:3381px"><h4>Lorem Ipsum is simply dummy text.</h4><p>Lorem Ipsum is simply dummy text of the printing and typesetting industry. Lorem Ipsum has been the industry's standard dummy text ever since the 1500s.</p><div class="btn">Read More</div></article>
<article class="news" style="left:461px;top:3381px"><h4>Lorem Ipsum is simply dummy text.</h4><p>Lorem Ipsum is simply dummy text of the printing and typesetting industry. Lorem Ipsum has been the industry's standard dummy text ever since the 1500s.</p><div class="btn">Read More</div></article>
<article class="news" style="left:161px;top:3644px"><h4>Lorem Ipsum is simply dummy text.</h4><p>Lorem Ipsum is simply dummy text of the printing and typesetting industry. Lorem Ipsum has been the industry's standard dummy text ever since the 1500s.</p><div class="btn">Read More</div></article>
<article class="news" style="left:461px;top:3644px"><h4>Lorem Ipsum is simply dummy text.</h4><p>Lorem Ipsum is simply dummy text of the printing and typesetting industry. Lorem Ipsum has been the industry's standard dummy text ever since the 1500s.</p><div class="btn">Read More</div></article>

<!-- footer -->
<footer class="abs footer"></footer>
<div class="abs brand footer-logo">BRIGHTWAVE LINK <span class="mark"></span></div>
<nav class="nav" style="left:0;top:4228px;color:#fff">
  <span style="left:394px">Home</span><span style="left:453px">Why Us?</span><span style="left:526px">Products</span><span style="left:600px">Resources</span><span style="left:685px">News</span><span style="left:745px">Contact Us</span>
</nav>
<div class="abs footer-rule"></div>
<div class="abs follow">FOLLOW US ON</div>
<div class="social" style="left:513px" aria-label="Social link"><i></i></div>
<div class="social active" style="left:560px" aria-label="Social link"><i></i></div>
<div class="social" style="left:604px" aria-label="Social link"><i></i></div>
<div class="social" style="left:649px" aria-label="Social link"><i></i></div>
<div class="abs legal">Copyright ©2020 Tandemvexa. All Rights Reserved.Terms &amp; Conditions.</div>

</body>
</html>
```